Willowmere Haven tri-fold brochure

We are a small assisted living in a home-like environment. Brochure should be warm, heartfelt and include the list of services we provide (see existing brochure). I also want the front picture replaced with stock photo (so no picture of owners). New name to use (instead of Hester) is Dorian Feltrowe, and email is feltrowe@quintmail.example. Address is same. If you can find better photos, that would be good, all the photos here are dated. We are looking for a more professional design that still conveys warmth, because we are in a home-setting and only care for 9 residents.

Target Market(s)

35-55 year old children looking for an assisted living because their parents are unable to care for them.

Industry/Entity Type

Environment

Contact Information for Business Card

Dorian Feltrowe
Willowmere Haven or Willowmere Haven Assisted Living
40718 Pinegrove Ln. Conroe, TX 77519
281-647-5192

Requirements
Must have
• List of services offered (feel free to re-word or add/change)
• Be sure to change "Hester/Hestie" to Dorian / Dorian Feltrowe

```html
<!DOCTYPE html>
<html lang="en">
<head>
<meta charset="utf-8">
<title>Willowmere Haven Tri-fold Brochure</title>
<link rel="stylesheet" href="https://fonts.googleapis.com/css2?family=Playball&family=Pathway+Gothic+One&family=Raleway:wght@400;500;600&display=swap">
<style>
:root{
  --lavender:#8b86d2;
  --lavender-soft:#a9a5e0;
  --gold:#e9b949;
  --ink:#3a3a3a;
  --body:#555;
  --paper:#fff;
  --panel-shade:#f6f6f6;
  --stage:#e7e5e1;
}
*{box-sizing:border-box;margin:0;padding:0}
html,body{width:960px;height:1200px;overflow:hidden}
body{position:relative;background:var(--stage);font-family:"Raleway",sans-serif;color:var(--body)}
.brochure{position:absolute;left:96px;top:54px;width:820px;height:1173px;transform:scale(0.9317);transform-origin:0 0}
.sheet{position:relative;width:820px;height:580px;display:grid;grid-template-columns:repeat(3,1fr);background:var(--paper);box-shadow:0 4px 14px rgba(0,0,0,.18);overflow:hidden}
.sheet + .sheet{margin-top:13px}
.panel{position:relative;overflow:hidden}
.panel--shaded{background:linear-gradient(90deg,var(--panel-shade),#fff 30%)}
.script{font-family:"Playball",cursive;font-weight:400;line-height:1.05}
.script--gold{color:var(--gold)}
.script--lav{color:var(--lavender)}
.photo{position:absolute;border-radius:50%}
.btn{position:absolute;height:26px;border-radius:7px;background:linear-gradient(#b0ace6,var(--lavender));color:#fff;font-weight:600;font-size:15px;text-align:center;line-height:26px;letter-spacing:.5px;box-shadow:0 2px 3px rgba(0,0,0,.2)}

/* Testimonials */
.testimonials h2{position:absolute;top:22px;width:100%;text-align:center;font-size:30px}
.quotes{position:absolute;top:66px;left:0;right:6px;list-style:none}
.quotes li{position:relative;padding-left:38px;font-size:9.6px;line-height:1.32;margin-bottom:7px}
.quotes li::before{content:"";position:absolute;left:0;top:0;width:28px;height:14px;background:var(--lavender-soft)}
.testimonials .lead{position:absolute;top:312px;width:100%;text-align:center;font-size:11px;line-height:1.45;color:var(--ink)}
.testimonials .instinct{position:absolute;top:344px;width:100%;text-align:center;font-size:21px;color:var(--lavender)}
.testimonials .photo-band{position:absolute;left:0;right:0;top:374px;bottom:0;background:linear-gradient(135deg,#e9e1d8,#c8b3a2 55%,#8f7566)}

/* Contact panel */
.contact h2{position:absolute;top:26px;width:100%;text-align:center;font-size:26px;color:#4a4a55}
.contact h2 em{font-style:normal;color:var(--lavender)}
.contact .photo{left:50px;top:148px;width:166px;height:166px;background:radial-gradient(circle at 55% 55%,#b07a55,#6b3e22 60%,#3a2014);border:4px solid transparent;border-bottom-color:var(--gold);border-left-color:var(--gold)}
.tour{position:absolute;left:0;right:0;text-align:center;color:var(--ink);font-weight:600;font-size:13.5px;line-height:1.2}
.tour .big{display:block;font-size:19px;font-weight:500}
.tour .name{font-family:"Playball",cursive;font-weight:400;color:var(--lavender);font-size:15px}
.contact .tour{top:355px}
.contact .tour .big{color:var(--lavender)}
.contact-list{position:absolute;top:422px;width:100%;list-style:none;text-align:center;font-size:12.5px;color:var(--ink)}
.contact-list li{margin-bottom:12px;line-height:1.35}
.contact-list svg{display:block;margin:0 auto 2px}
.contact-list .phone{font-size:15px}

/* Cover */
.cover .brand{position:absolute;top:22px;width:100%;text-align:center}
.cover .brand .script{font-size:33px;color:var(--lavender)}
.cover .brand .tag{font-family:"Pathway Gothic One",sans-serif;font-size:22px;color:#444;margin-top:2px}
.cover .photo--main{left:-8px;top:106px;width:296px;height:296px;background:linear-gradient(160deg,#7c8a55,#b7a27e 45%,#c68a66 70%,#6d7a92);border:4px solid transparent;border-bottom-color:var(--gold);border-left-color:var(--gold)}
.cover .photo--small{left:-4px;top:324px;width:136px;height:136px;background:linear-gradient(140deg,#e8eef3,#7fb4d6 55%,#4c86b4);border:4px solid #fff;box-shadow:0 0 0 3px var(--gold)}
.cover .promise{position:absolute;right:12px;top:414px;text-align:right;font-size:15px;line-height:1.2;color:#444}
.cover .promise b{font-weight:500;color:var(--lavender)}
.cover .call{position:absolute;left:16px;top:532px;font-size:13px;line-height:1.1;color:#444}
.cover .btn{left:80px;top:535px;width:180px}

/* Why panel */
.why .photo{left:-150px;top:-250px;width:490px;height:490px;background:linear-gradient(150deg,#f2efe9,#d9d3c8 40%,#8aa0bb 70%,#5b6e8c);border:8px solid transparent;border-bottom-color:var(--lavender-soft)}
.why h2{position:absolute;top:290px;left:22px;font-size:23px}
.why .copy{position:absolute;top:320px;left:16px;right:16px;font-size:10.8px;line-height:1.32;text-align:justify}
.why .copy p{margin-bottom:10px}
.why .btn{left:46px;top:528px;width:180px}

/* Services */
.services h2{position:absolute;top:36px;width:100%;text-align:center;font-size:32px}
.service-list{position:absolute;top:84px;left:24px;right:14px;list-style:none}
.service-list li{position:relative;padding-left:10px;font-size:12.2px;line-height:1.05;margin-bottom:12px;color:#555}
.service-list li::before{content:"";position:absolute;left:0;top:4px;width:3px;height:3px;border-radius:50%;background:var(--gold)}
.services .tour{top:482px;text-align:left;left:20px}
.services .tour .big{color:var(--gold)}
.services .tour .name{font-size:23px;display:block}

/* Home panel */
.home h2{position:absolute;top:38px;width:100%;text-align:center;font-size:27px}
.home .copy{position:absolute;top:114px;left:20px;right:18px;font-size:10.8px;line-height:1.32}
.home .copy p{margin-bottom:12px}
.home .photo{left:76px;top:402px;width:250px;height:250px;background:linear-gradient(140deg,#d8c7b3,#9a7a68 45%,#5a6d9c 70%,#c9bdb3);border:6px solid transparent;border-left-color:var(--gold);border-top-color:var(--gold)}
</style>
</head>
<body>
<main class="brochure">

  <section class="sheet sheet--outside">
    <div class="panel testimonials">
      <h2 class="script script--gold">Testimonials</h2>
      <ul class="quotes">
        <li>My mom lived in five private care homes. When she moved here she said: "I've finally found my home!". Thank you!<br>-Marian T.</li>
        <li>I am so happy that I found you! I can't imagine my mom being anywhere else. Everyone there is loving and respectful and they really care about all the residents. For my mom, I know that she was happy and at peace with such amazing people around her. Thank you so much...<br>-Delia R.</li>
        <li>Willowmere Haven lives up to its name. I will never forget the compassionate, hard work and love you shared with my dad. Words cannot express how happy I am to have found you.<br>-Howard P.</li>
      </ul>
      <p class="lead">If you are one of the millions of people<br>who feel this way, We say,</p>
      <p class="instinct script">"Trust your instincts"</p>
      <div class="photo-band" role="img" aria-label="Photo of an elderly woman and a young caregiver doing a jigsaw puzzle together at a table"></div>
    </div>

    <div class="panel panel--shaded contact">
      <h2 class="script"><em>Smaller</em> is better<br>when it comes to<br>the <em>elderly</em></h2>
      <div class="photo" role="img" aria-label="Close-up photo of a young hand holding an elderly hand"></div>
      <p class="tour"><span class="big">CALL FOR A PERSONAL</span>TOUR AND EXPERIENCE THE<br><span class="name">Willowmere Haven</span> DIFFERENCE.</p>
      <ul class="contact-list">
        <li><svg width="10" height="13" viewBox="0 0 10 13"><path d="M5 0a5 5 0 0 0-5 5c0 3.5 5 8 5 8s5-4.5 5-8a5 5 0 0 0-5-5zm0 7a2 2 0 1 1 0-4 2 2 0 0 1 0 4z" fill="#e9b949"/></svg>40718 Pinegrove Ln.<br>Conroe, Texas</li>
        <li><svg width="11" height="8" viewBox="0 0 11 8"><rect width="11" height="8" rx="1" fill="#e9b949"/><path d="M0 0l5.5 4.5L11 0" stroke="#fff" fill="none"/></svg>feltrowe@quintmail.example</li>
        <li class="phone"><svg width="11" height="9" viewBox="0 0 11 9"><path d="M0 3c0-2 2-3 5.5-3S11 1 11 3H8V2H3v1zM2 4h7l1 5H1z" fill="#e9b949"/></svg>281-647-5192</li>
      </ul>
    </div>

    <div class="panel cover">
      <div class="brand">
        <div class="script">Willowmere Haven</div>
        <div class="tag">Assisted Living &amp; Memory Care</div>
      </div>
      <div class="photo photo--main" role="img" aria-label="Stock photo of a smiling caregiver greeting a senior man in a wheelchair outdoors"></div>
      <div class="photo photo--small" role="img" aria-label="Stock photo of a nurse and a senior woman smiling together"></div>
      <p class="promise">Offering a <b>true<br>and noble<br>commitment</b><br>to the highest<br>standards of care<br>in the industry.</p>
      <p class="call">Call<br>Dorian</p>
      <div class="btn">281-647-5192</div>
    </div>
  </section>

  <section class="sheet sheet--inside">
    <div class="panel why">
      <div class="photo" role="img" aria-label="Photo of a nurse helping a senior man with his leg on a sofa"></div>
      <h2 class="script script--gold">Why Willowmere Haven?</h2>
      <div class="copy">
        <p>Choosing the right place for your loved one is an important decision. Willowmere Haven is here to help give you peace of mind.</p>
        <p>Innovative care in a residential environment provides a wonderful alternative to institutional living. Our residents truly become a family because of the small, intimate, home-like atmosphere.</p>
        <p>Our first concern is making life safe, comfortable and enjoyable for those who have been entrusted to us.</p>
      </div>
      <div class="btn">281-647-5192</div>
    </div>

    <div class="panel panel--shaded services">
      <h2 class="script script--lav">Services</h2>
      <ul class="service-list">
        <li>Medical supervision provided by visiting physicians and nursing personnel</li>
        <li>Rehabilitation, home health and hospice services available through licensed professionals</li>
        <li>Medications and incontinence management</li>
        <li>Personal attention, caregiver involvement and heightened activities focusing on hobbies, crafts, exercise, music therapy, holiday and birthday celebrations, and plant and pet therapy.</li>
        <li>Nutritious home cooked meals and snacks with emphasis on hydration.</li>
        <li>Assistance with bathing, grooming and other personal needs including daily laundry and housekeeping.</li>
      </ul>
      <p class="tour"><span class="big">CALL FOR A PERSONAL</span>TOUR AND EXPERIENCE THE<span class="name">Willowmere Haven</span>DIFFERENCE.</p>
    </div>

    <div class="panel panel--shaded home">
      <h2 class="script script--gold">Willowmere Haven is<br>Your Home</h2>
      <div class="copy">
        <p>The comforts of home in a private luxurious setting, allows loving care with dignity</p>
        <p>Private or companion rooms, elegantly furnished or personalized to your style.</p>
        <p>A living room, family room, dining room, sunroom, and kitchen residents can call their own, so they can live the way they always have.</p>
        <p>Enjoy beautiful days on the patio and in the lovely garden area with beautiful trees, flowers, birds and pets.</p>
      </div>
      <div class="photo" role="img" aria-label="Photo of seniors stretching their arms during a group exercise class"></div>
    </div>
  </section>

</main>
</body>
</html>
```